Home Design company focused on remodel and enhancement of kitchens and bathroorms

I already have a logo designed by ArtHarbor, I now need a design for my business cards.
The company is in the remodeling and enhancement industry for homes, focusing on kitchens and bathrooms, however, we can remodel or enhance every room in a home, an office space, etc.

The company's name is VELMOR HOME DESIGN, LLC

We'll focus on clients in the Rio Grande Valley, Texas. Primarily McAllen, Edinburg, Pharr, Mission, Brownsville and South Padre Island.

The design on the business card should transmit reliability, professionalism anda bit of upscale design.

The logo is in black and white, and would like to keep it that way.

The information that needs to be printed in the business cards is:
Company's name: Velmor Home Design
Company's Logo (attached)
My name: Noel Bramwit
Address, phone and email:
2715 N Parkline Road, Ste 348
McAllen, TX 78501
(956) 555 0187
nbramwit@velmordesign.example
Website: velmordesign.example

```html
<!DOCTYPE html>
<html lang="en">
<head>
<meta charset="utf-8">
<title>Velmor Home Design – Business Cards</title>
<link rel="stylesheet" href="https://fonts.googleapis.com/css2?family=Lato:wght@400;700&display=swap">
<style>
  :root {
    --backdrop: #2e2e2e;
    --card: #1b1b1b;
    --ink: #ffffff;
    --ink-soft: #e6e6e6;
    --emboss: #141414;
    --emboss-edge: #262626;
  }
  * { margin: 0; padding: 0; box-sizing: border-box; }
  html, body { width: 1200px; height: 1015px; overflow: hidden; }
  body {
    background: var(--backdrop);
    font-family: "Lato", sans-serif;
    color: var(--ink);
    position: relative;
  }
  .card {
    position: absolute;
    left: 250px;
    width: 700px;
    height: 400px;
    background: var(--card);
    overflow: hidden;
  }
  .card--front { top: 80px; }
  .card--back { top: 535px; }

  /* Front */
  .brand {
    position: absolute;
    left: 0; right: 0; top: 50%;
    transform: translateY(-50%);
    display: flex;
    align-items: center;
    justify-content: center;
    gap: 22px;
  }
  .brand__square {
    width: 34px; height: 34px;
    border: 3px solid var(--ink);
  }
  .brand__name {
    font-weight: 400;
    font-size: 30px;
    letter-spacing: 8px;
    color: var(--ink);
  }

  /* Back */
  .watermark {
    position: absolute;
    right: 40px;
    top: 60px;
    font-weight: 700;
    font-size: 96px;
    letter-spacing: 6px;
    color: var(--emboss);
    text-shadow: 1px 1px 0 var(--emboss-edge);
  }
  .contact {
    position: absolute;
    left: 56px;
    top: 120px;
    font-size: 19px;
    line-height: 1.25;
    color: var(--ink-soft);
  }
  .contact__person {
    font-weight: 700;
    font-size: 23px;
    letter-spacing: 0.5px;
    color: var(--ink);
    margin-bottom: 30px;
  }
  .contact__company {
    font-weight: 700;
    color: var(--ink);
  }
  .contact__address { margin-bottom: 30px; }
  .contact__list { list-style: none; }
  .contact__item {
    display: flex;
    align-items: center;
    gap: 10px;
  }
  .contact__icon { width: 18px; height: 18px; flex: none; }
</style>
</head>
<body>
  <section class="card card--front">
    <div class="brand">
      <span class="brand__square"></span>
      <span class="brand__name">VELMOR HOME DESIGN</span>
    </div>
  </section>

  <section class="card card--back">
    <div class="watermark" aria-hidden="true">VELMOR</div>
    <div class="contact">
      <p class="contact__person">NOEL BRAMWIT</p>
      <div class="contact__address">
        <p class="contact__company">VELMOR HOME DESIGN</p>
        <p>2715 N Parkline Road, Ste 348</p>
        <p>McAllen, TX 78501</p>
      </div>
      <ul class="contact__list">
        <li class="contact__item">
          <svg class="contact__icon" viewBox="0 0 24 24" fill="none" stroke="currentColor" stroke-width="2" stroke-linejoin="round"><path d="M5 3h4l2 5-2.5 1.5a11 11 0 0 0 6 6L16 13l5 2v4a2 2 0 0 1-2 2A16 16 0 0 1 3 5a2 2 0 0 1 2-2z"/></svg>
          <span>(956) 555 0187</span>
        </li>
        <li class="contact__item">
          <svg class="contact__icon" viewBox="0 0 24 24" fill="none" stroke="currentColor" stroke-width="2"><rect x="2" y="5" width="20" height="14"/><path d="M2 5l10 8 10-8"/></svg>
          <span>nbramwit@velmordesign.example</span>
        </li>
        <li class="contact__item">
          <svg class="contact__icon" viewBox="0 0 24 24" fill="none" stroke="currentColor" stroke-width="2"><circle cx="12" cy="12" r="10"/><path d="M2 12h20M12 2c3 3 3 17 0 20M12 2c-3 3-3 17 0 20"/></svg>
          <span>www.velmordesign.example</span>
        </li>
      </ul>
    </div>
  </section>
</body>
</html>
```